Skip Bin Hire Business

We are an existing business that hire out skip bins for domestic and commercial use. We are looking for a fresh look with no colours or designs in mind.
We have 2m3 and 3m3 skip bins and 3m3 up to 24m3 walk in bins.
Visit our website for more information.
www.harborcrate.com.au
We are going to add a photo of a 3m3 skip as this is a new product for our company and not available on our website at this stage.

Industry/Entity Type

Business

Contact Information for Business Card

Harbor Crate
9172-4086
www.harborcrate.com.au

```html
<!DOCTYPE html>
<html lang="en">
<head>
<meta charset="utf-8">
<title>Harbor Crate – Business Card</title>
<link rel="stylesheet" href="https://fonts.googleapis.com/css2?family=Roboto:wght@300;400&display=swap">
<style>
  :root {
    --page-bg: #e9e6e1;
    --card-dark: #1f1f21;
    --card-mid: #3a3a3d;
    --accent-yellow: #f2c81f;
    --text-light: #f1f1f1;
    --text-dark: #1e1e1e;
  }
  html, body {
    margin: 0;
    padding: 0;
    width: 1200px;
    height: 996px;
    overflow: hidden;
    background: var(--page-bg);
    font-family: "Roboto", Arial, sans-serif;
  }
  .business-card {
    position: absolute;
    left: 75px;
    top: 198px;
    width: 1050px;
    height: 600px;
    overflow: hidden;
    background: linear-gradient(100deg, var(--card-dark) 0%, var(--card-mid) 42%, var(--card-dark) 75%, #151516 100%);
    box-shadow: 0 10px 30px rgba(0,0,0,0.25);
  }
  .accent-block-left {
    position: absolute;
    left: 0;
    top: 105px;
    width: 92px;
    height: 85px;
    background: var(--accent-yellow);
  }
  .accent-bar-top {
    position: absolute;
    left: 592px;
    top: 30px;
    width: 458px;
    height: 160px;
    background: var(--accent-yellow);
  }
  .company-name {
    position: absolute;
    left: 112px;
    top: 112px;
    margin: 0;
    font-weight: 400;
    font-size: 66px;
    line-height: 80px;
    color: var(--text-light);
    letter-spacing: 0.5px;
  }
  .contact-list {
    position: absolute;
    left: 420px;
    top: 236px;
    margin: 0;
    padding: 0;
    list-style: none;
  }
  .contact-item {
    display: flex;
    align-items: center;
    height: 58px;
    font-weight: 300;
    font-size: 30px;
    color: var(--text-light);
  }
  .contact-icon {
    width: 24px;
    height: 24px;
    margin-right: 18px;
    fill: var(--text-light);
    flex: none;
  }
  .footer-band {
    position: absolute;
    left: 0;
    bottom: 0;
    width: 100%;
    height: 78px;
    background: var(--accent-yellow);
  }
  .website {
    position: absolute;
    right: 215px;
    top: 20px;
    font-weight: 400;
    font-size: 30px;
    color: var(--text-dark);
  }
</style>
</head>
<body>
  <section class="business-card" aria-label="Harbor Crate business card">
    <div class="accent-block-left"></div>
    <div class="accent-bar-top"></div>
    <h1 class="company-name">Harbor Crate</h1>

    <ul class="contact-list">
      <li class="contact-item">
        <svg class="contact-icon" viewBox="0 0 24 24" aria-hidden="true"><path d="M12 1a8 8 0 0 0-8 8c0 6 8 14 8 14s8-8 8-14a8 8 0 0 0-8-8zm0 11a3 3 0 1 1 0-6 3 3 0 0 1 0 6z"/></svg>
        14 Dockside Road, Preston Victoria. 3072.
      </li>
      <li class="contact-item">
        <svg class="contact-icon" viewBox="0 0 24 24" aria-hidden="true"><path d="M6.6 10.8a15 15 0 0 0 6.6 6.6l2.2-2.2a1 1 0 0 1 1-.25 11.4 11.4 0 0 0 3.6.6 1 1 0 0 1 1 1V20a1 1 0 0 1-1 1A17 17 0 0 1 3 4a1 1 0 0 1 1-1h3.5a1 1 0 0 1 1 1c0 1.25.2 2.45.6 3.6a1 1 0 0 1-.25 1z"/></svg>
        (03) 9172 4086
      </li>
      <li class="contact-item">
        <svg class="contact-icon" viewBox="0 0 24 24" aria-hidden="true"><path d="M2 5h20v14H2z" fill="none"/><path d="M2 5h20L12 13z"/><path d="M2 7l10 8 10-8v12H2z"/></svg>
        admin@harborcrate.com.au
      </li>
    </ul>

    <div class="footer-band">
      <span class="website">www.harborcrate.com.au</span>
    </div>
  </section>
</body>
</html>
```